Centro Renal Tova Quirandel

Redo a rough draft of the presentation. Some slides are just hand sketches. 15 slides total

Font styles to use
Sans Serif

Colors

Designer to choose colors to be used in the design.

Requirements
Must have
• Use the 'machine' on the dialysis slide. The kidney wherever you feel works to accentuate.
• The slide following the 'supporting cast' should be the same but 'centro vitrales norteños' in bold and maybe the picture vascular acces if works.
• Use the 4 puerto Halcón pictures for 'centro de dialisis puerto halcón' create 4 slides using one picture per slide; go big.
• Create a location slide before the last q&a slide using the location picture
Nice to have
• Please use elegant font for title
• Create something for the estadisticas 2016 slides; not a list like it is now

```html
<!DOCTYPE html>
<html lang="en">
<head>
<meta charset="utf-8">
<title>Slide – Image Title</title>
<link rel="stylesheet" href="https://fonts.googleapis.com/css2?family=Lato:wght@400;700&display=swap">
<style>
  :root {
    --canvas-width: 1200px;
    --canvas-height: 900px;
    --accent-red: #d7171c;
    --accent-red-deep: #c51217;
    --text-light: #ffffff;
    --photo-light: #e9e8ee;
    --photo-mid: #b9b3c6;
    --photo-dark: #7d7590;
  }

  html, body {
    margin: 0;
    padding: 0;
    width: var(--canvas-width);
    height: var(--canvas-height);
    overflow: hidden;
    background: #ffffff;
  }

  .slide {
    position: relative;
    width: var(--canvas-width);
    height: var(--canvas-height);
    overflow: hidden;
    font-family: "Lato", Arial, sans-serif;
  }

  .slide__photo {
    position: absolute;
    inset: 0;
    background:
      radial-gradient(ellipse 40% 35% at 22% 70%, var(--photo-mid) 0%, transparent 70%),
      radial-gradient(ellipse 30% 40% at 52% 45%, var(--photo-mid) 0%, transparent 70%),
      linear-gradient(170deg, var(--photo-light) 0%, #d4d0dc 45%, var(--photo-dark) 100%);
  }

  .slide__panel {
    position: absolute;
    top: 0;
    left: 600px;
    width: 600px;
    height: 900px;
    background: linear-gradient(180deg, var(--accent-red) 0%, var(--accent-red-deep) 100%);
    box-sizing: border-box;
    padding: 168px 48px 0 48px;
    color: var(--text-light);
  }

  .slide__title {
    margin: 0 0 14px 0;
    font-weight: 700;
    font-size: 51px;
    line-height: 1.15;
    letter-spacing: 0.2px;
    text-transform: uppercase;
  }

  .slide__body {
    margin: 0;
    font-weight: 400;
    font-size: 28px;
    line-height: 48px;
    text-align: justify;
    hyphens: manual;
  }
</style>
</head>
<body>
  <main class="slide">
    <div class="slide__photo" role="img" aria-label="Close-up photo of a dialysis machine with its pumps, tubing and control display"></div>

    <section class="slide__panel">
      <h1 class="slide__title">Image Title Here</h1>
      <p class="slide__body">Lorem Ipsum is simply dummy text of the printing and typesetting in&shy;dustry. Lorem Ipsum has been the in&shy;dustry's standard dummy text ever since the 1500s, when an unknown printer took a galley of type and scrambled it to make a type speci&shy;men book.</p>
    </section>
  </main>
</body>
</html>
```